web page template design

We'd like to see a few designs based on the selected logo. See attached color logo.

We'll need a homepage design which will display the competition announcement and limited details about it. There will be links (or tabs) to the follow on pages which will contain all of the legal details, sign-up and design submission page, finalist selection page, winner announcement page, jury (judges) background page, company sponsor (Verant) details, press release page and a blog page. These are just guidelines for the number of subpage links.

So we'd like a primary page and a follow-on page which is a little more plain.

Here is the competition briefer below:

In January 2014, Verant Tile Inc. will launch its 1st Annual Verant Tile Floor Design Competition. This design competition will be open to Design and Architecture students of the NYC area. Students and student groups can submit cork flooring design concepts online to a judging committee of prominent designers and architects who will select design finalists and a winner. The winning design will highlight the unique creative possibilities of sustainable cork tiles. The winner will receive a cash prize and publication of their winning design through press releases and various media outlets as well as on the PlankMosaic.example website. The winning floor will be created and photographed by Verant Tile and will be donated to a deserving non-profit community center in NYC. The donated cork floor will be installed at no cost to the non-profit community center.

Target Market(s)

designers and architects.

Industry/Entity Type

Non-Profit

Requirements
Must have
• tabs or link system

```html
<!DOCTYPE html>
<html lang="en">
<head>
<meta charset="utf-8">
<title>Verant Tile Floor Design Competition 2014</title>
<link rel="stylesheet" href="https://fonts.googleapis.com/css2?family=Open+Sans:wght@400;600&family=Raleway:wght@400;500;700&display=swap">
<style>
  :root {
    --page-bg: #fafafa;
    --hero-bg: #f1f1f1;
    --ink: #3a3a3a;
    --ink-soft: #555555;
    --brand-brown: #4a2f22;
    --accent-gold: #c8922a;
    --accent-red: #8e2422;
    --button: #c67a2f;
    --signup-link: #6b3a1c;
    --social: #666666;
    --rule: #e2e2e2;
    --floor-light: #c98a4e;
    --floor-dark: #a65a1c;
  }
  * { box-sizing: border-box; margin: 0; padding: 0; }
  html, body { width: 1200px; height: 675px; overflow: hidden; }
  body {
    background: var(--page-bg);
    font-family: "Open Sans", Arial, sans-serif;
    color: var(--ink);
    position: relative;
  }

  .site-header {
    position: absolute; left: 0; top: 0; width: 1200px; height: 124px;
    background: var(--page-bg);
    border-bottom: 1px solid var(--rule);
    box-shadow: 0 1px 3px rgba(0,0,0,0.06);
    z-index: 2;
  }
  .brand {
    position: absolute; left: 155px; top: 24px; width: 150px;
    display: flex; flex-direction: column; align-items: center;
    font-family: "Raleway", Arial, sans-serif; font-weight: 700;
    color: var(--brand-brown); text-align: center;
  }
  .brand-mark {
    width: 48px; height: 48px; border-radius: 50%;
    background: var(--brand-brown); margin-bottom: 8px;
  }
  .brand-name { font-size: 13px; line-height: 15px; }
  .brand-sub { font-size: 7px; letter-spacing: 2.4px; line-height: 10px; }

  .utility-nav {
    position: absolute; right: 164px; top: 37px;
    font-family: "Raleway", Arial, sans-serif; font-size: 13.5px;
    color: var(--ink);
  }
  .utility-nav a { color: var(--ink); text-decoration: none; }
  .utility-nav a.signup { color: var(--signup-link); }
  .utility-nav .divider { margin: 0 10px; }

  .main-nav {
    position: absolute; right: 164px; top: 79px;
    display: flex; gap: 15.5px;
    font-family: "Raleway", Arial, sans-serif; font-size: 13.5px;
  }
  .main-nav a { color: var(--ink); text-decoration: none; }

  .hero {
    position: absolute; left: 0; top: 124px; width: 1200px; height: 481px;
    background: var(--hero-bg);
  }
  .announcement { position: absolute; left: 155px; top: 130px; }
  .announcement .lead { font-size: 16px; color: var(--ink); line-height: 30px; }
  .announcement .company { font-size: 23px; color: var(--accent-gold); }
  .announcement h1 {
    font-weight: 400; font-size: 23px; line-height: 35px;
    color: var(--accent-red); margin-top: 2px;
  }
  .announcement .date { font-size: 16px; line-height: 26px; margin-top: 5px; }
  .announcement .date a { color: var(--accent-gold); }

  .cta {
    position: absolute; left: 155px; top: 296px;
    width: 149px; height: 39px;
    background: var(--button); color: #fff;
    font-family: "Raleway", Arial, sans-serif; font-size: 16px;
    display: flex; align-items: center; justify-content: center; gap: 6px;
    text-decoration: none; border-radius: 1px;
  }

  .hero-visual {
    position: absolute; left: 446px; top: 56px; width: 590px; height: 371px;
    background: linear-gradient(180deg, var(--floor-light), var(--floor-dark));
  }

  .site-footer {
    position: absolute; left: 0; top: 605px; width: 1200px; height: 70px;
    background: var(--page-bg); border-top: 1px solid var(--rule);
  }
  .copyright {
    position: absolute; left: 155px; top: 26px;
    font-size: 11.5px; line-height: 16px; color: var(--ink-soft);
  }
  .social { position: absolute; left: 945px; top: 22px; display: flex; gap: 6px; }
  .social a { width: 27px; height: 27px; border-radius: 50%; background: var(--social); display: block; }
</style>
</head>
<body>
  <header class="site-header">
    <a class="brand" aria-label="Verant Tile Floor Design Competition 2014">
      <span class="brand-mark"></span>
      <span class="brand-name">VERANT TILE FLOOR</span>
      <span class="brand-sub">DESIGN COMPETITION</span>
      <span class="brand-sub">2014</span>
    </a>
    <nav class="utility-nav">
      <a class="signup" href="#">Signup</a><span class="divider">|</span><a href="#">Terms &amp; Policy</a>
    </nav>
    <nav class="main-nav">
      <a href="#">Submit design</a>
      <a href="#">The Finalist</a>
      <a href="#">Winner</a>
      <a href="#">The Jury</a>
      <a href="#">Our Sponsor</a>
      <a href="#">Press Release</a>
      <a href="#">Blog</a>
    </nav>
  </header>

  <section class="hero">
    <div class="announcement">
      <p class="lead"><span class="company">Verant Tile Inc.</span> announcing its</p>
      <h1>1st Annual Verant Tile<br>Floor Design Competition</h1>
      <p class="date">On <a href="#">January 2014.</a></p>
    </div>
    <a class="cta" href="#">Signup Now
      <svg width="12" height="12" viewBox="0 0 12 12" aria-hidden="true"><path d="M2 2l4 4-4 4M6 2l4 4-4 4" fill="none" stroke="#fff" stroke-width="1.6"/></svg>
    </a>

    <div class="hero-visual" role="img" aria-label="Illustration of three young designers sketching at a desk placed on a curved wooden cork floor"></div>
  </section>

  <footer class="site-footer">
    <p class="copyright">Copyright@2013, VERANT</p>
    <nav class="social" aria-label="Social links">
      <a href="#" aria-label="Social profile one"></a>
      <a href="#" aria-label="Social profile two"></a>
      <a href="#" aria-label="Social profile three"></a>
    </nav>
  </footer>
</body>
</html>
```